website for 'thebrightnook' which is a specialise tutoring company for children with learning difficu

We need a website for a new business that is focused on assessment and then specialised tutoring for young children with learning difficulties. The website needs to be simple but fun and fresh. We have an existing logo (uploaded) that needs to be the building block for the website. The website doesn't need to be overly content-heavy.

Target Market(s)

parents

Industry/Entity Type

Education

Number of Pages Required

3 page

Font styles to use
Other font styles liked:
• possibly matched to the logo

Requirements
Must have
• a initial front page which introduces the business and provides contact details, a second page that will allow for a more content-heavy section, a third page which focuses on introducing the staff (initially 3 staff ),

```html
<!DOCTYPE html>
<html lang="en">
<head>
<meta charset="utf-8">
<title>thebrightnook – science: exploring volume</title>
<link rel="stylesheet" href="https://fonts.googleapis.com/css2?family=Rokkitt:wght@400;500&family=Arimo:wght@400;700&family=Crimson+Text&family=Lora:ital@1&display=swap">
<style>
  :root {
    --green: #80c241;
    --green-dark: #4f8f1c;
    --ink: #222222;
    --text: #333333;
    --muted: #6d6d6d;
    --paper: #f3f0e8;
    --tan: #c9b797;
    --white: #ffffff;
    --frame: #ffffff;
    --rule: #cfcfcf;
  }
  * { box-sizing: border-box; margin: 0; padding: 0; }
  html, body { width: 1200px; height: 1061px; overflow: hidden; }
  body { position: relative; background: var(--paper); font-family: "Arimo", Arial, sans-serif; color: var(--text); }

  .site-header { position: absolute; left: 0; top: 0; width: 1200px; height: 220px; background: var(--white); }
  .brand-name { position: absolute; left: 116px; top: 112px; font-family: "Rokkitt", serif; font-weight: 400; font-size: 52px; color: var(--muted); letter-spacing: -1px; line-height: 1; }
  .brand-tagline { position: absolute; left: 116px; top: 173px; font-family: "Rokkitt", serif; font-size: 14px; letter-spacing: 2.4px; color: var(--muted); white-space: nowrap; }

  .utility { position: absolute; top: 12px; left: 0; width: 1200px; height: 30px; }
  .social-dot { position: absolute; width: 28px; height: 28px; border-radius: 50%; background: var(--green); }
  .utility .divider { position: absolute; top: 4px; width: 1px; height: 22px; background: #cccccc; }
  .subscribe { position: absolute; left: 980px; top: 6px; font-family: "Lora", serif; font-style: italic; font-size: 16px; color: var(--muted); }

  .main-nav { position: absolute; top: 166px; right: 120px; height: 36px; display: flex; align-items: center; }
  .main-nav a { display: block; height: 36px; line-height: 36px; padding: 0 14px; font-family: "Rokkitt", serif; font-size: 18px; color: var(--ink); text-decoration: none; white-space: nowrap; }
  .main-nav a:last-child { padding-right: 0; }
  .main-nav a.is-active { background: var(--green); border-radius: 4px; padding: 0 8px; margin: 0 10px; }
  .main-nav .sep { width: 1px; height: 20px; background: var(--rule); }

  .band { position: absolute; left: 0; top: 220px; width: 1200px; height: 62px; }

  .photo-frame { position: absolute; background: var(--frame); border: 1px solid #dedad0; box-shadow: 0 4px 8px rgba(0,0,0,0.12); }
  .photo { position: absolute; }

  .lesson-title { position: absolute; left: 484px; top: 322px; width: 391px; height: 39px; background: var(--green); border-radius: 0 4px 4px 0; font-family: "Rokkitt", serif; font-weight: 500; font-size: 29px; color: var(--ink); line-height: 39px; padding-left: 30px; white-space: nowrap; overflow: hidden; }

  .lesson-body { position: absolute; left: 514px; top: 384px; width: 572px; }
  .supplies-title { font-size: 17px; font-weight: 700; color: #4a4a4a; }
  .supplies { list-style: none; margin: 12px 0 0 15px; font-size: 14.5px; line-height: 20.3px; color: #555555; }
  .lesson-body p { font-size: 15.6px; line-height: 25.8px; color: var(--ink); margin-top: 22px; }
  .lesson-body p + p { margin-top: 26px; }

  .lesson-links { position: absolute; left: 514px; top: 920px; font-size: 13px; color: var(--green-dark); white-space: nowrap; }
  .lesson-links .pipe { color: #aaaaaa; margin: 0 11px; }
  .filed { position: absolute; left: 516px; top: 969px; font-family: "Crimson Text", serif; font-size: 14.5px; color: #8a8a8a; white-space: nowrap; }
  .filed svg { vertical-align: -2px; margin-right: 4px; }

  .site-footer { position: absolute; left: 0; top: 1002px; width: 1200px; height: 59px; background: var(--tan); }
  .site-footer .social-dot { background: #9e9483; width: 27px; height: 27px; top: 16px; }
  .footer-brand { position: absolute; right: 120px; top: 8px; font-family: "Rokkitt", serif; font-size: 22px; letter-spacing: -0.5px; color: #5e574b; }
  .copyright { position: absolute; right: 120px; top: 38px; font-size: 12px; color: #5e574b; }
</style>
</head>
<body>
  <header class="site-header">
    <div class="utility">
      <span class="social-dot" style="left:806px;top:0"></span>
      <span class="social-dot" style="left:844px;top:0"></span>
      <span class="social-dot" style="left:882px;top:0"></span>
      <span class="divider" style="left:922px"></span>
      <svg style="position:absolute;left:932px;top:2px" width="30" height="26" viewBox="0 0 30 26" aria-label="basket">
        <rect x="10" y="1" width="10" height="6" fill="var(--green)"/>
        <rect x="2" y="8" width="26" height="4" fill="var(--green)"/>
        <path d="M4 13 H26 L24 25 H6 Z" fill="var(--green)"/>
      </svg>
      <span class="divider" style="left:970px"></span>
      <span class="subscribe">Subscribe</span>
      <svg style="position:absolute;left:1056px;top:4px" width="28" height="20" viewBox="0 0 28 20" aria-label="email">
        <rect x="0" y="0" width="28" height="20" fill="var(--green)"/>
        <path d="M0 0 L14 11 L28 0" fill="none" stroke="var(--white)" stroke-width="2"/>
      </svg>
    </div>

    <div class="brand-name">thebrightnook</div>
    <div class="brand-tagline">specialised learning for children</div>

    <nav class="main-nav">
      <a>home</a><span class="sep"></span>
      <a>about us</a><span class="sep"></span>
      <a>tutoring</a><span class="sep"></span>
      <a>assessments</a><span class="sep"></span>
      <a class="is-active">lesson plans</a><span class="sep"></span>
      <a>contact us</a>
    </nav>
  </header>

  <svg class="band" width="1200" height="62" viewBox="0 0 1200 62" aria-hidden="true">
    <defs>
      <pattern id="scallop" x="0" y="0" width="34" height="62" patternUnits="userSpaceOnUse">
        <path d="M0 0 H34 V44 A17 12 0 0 1 0 44 Z" fill="var(--tan)"/>
      </pattern>
      <filter id="band-shadow" x="-5%" y="-20%" width="110%" height="150%">
        <feDropShadow dx="0" dy="3" stdDeviation="2" flood-opacity="0.18"/>
      </filter>
    </defs>
    <rect width="1200" height="62" fill="var(--paper)"/>
    <rect width="1200" height="58" fill="url(#scallop)" filter="url(#band-shadow)"/>
  </svg>

  <div class="photo-frame" style="left:116px;top:320px;width:368px;height:526px">
    <div class="photo" role="img" aria-label="Young girl pouring blue liquid between glass flasks at a science table" style="left:9px;top:9px;width:346px;height:502px;background:linear-gradient(160deg,#e4e0da 0%,#c9b7a0 35%,#a88f74 60%,#5fa5c8 78%,#d9d2c4 100%)"></div>
  </div>

  <div class="photo-frame" style="left:116px;top:866px;width:366px;height:124px">
    <div class="photo" role="img" aria-label="Row of glass bottles and plastic containers filled with blue water" style="left:10px;top:9px;width:345px;height:104px;background:linear-gradient(90deg,#5d6d78 0%,#86b4d0 30%,#d6dde3 55%,#6fa3c6 80%,#c7d3dc 100%)"></div>
  </div>

  <h1 class="lesson-title">science: exploring volume</h1>

  <article class="lesson-body">
    <h2 class="supplies-title">Supplies you will need:</h2>
    <ul class="supplies">
      <li>* Plastic 1 or 2 Cup Measuring Container</li>
      <li>* Plastic Pitcher of Water</li>
      <li>* Funnel</li>
      <li>* Food Coloring</li>
      <li>* Variety of Containers in Different Sizes and Shapes</li>
      <li>* Tray and Paper Towels (To Catch Spills)</li>
    </ul>
    <p>Fill a plastic measuring jug with enough water the kids can manage pouring. We refilled our pitcher once. Add food coloring as desired. Adding a bit of color is fun for kids, and it helps them to see the volume of water in each container better. Place a variety of containers on a tray or table. I also set out a funnel to use with the water bottles. Water bottles, food storage containers, party cups, or any sort of clear container works great for this activity.</p>
    <p>Simple activities like this volume activity are a wonderful way to get kids thinking, exploring, problem solving, and observing what is happening around them. You can try this activity with a number of materials including small blocks, shells, gems, sand, and rocks. Setting up two stations, one for liquids and one for solids, is a great way for kids to explore volume with a variety of materials.</p>
  </article>

  <div class="lesson-links">
    <span>Go back to Science Lesson Plans</span><span class="pipe">|</span><span>Download Lesson Plan</span><span class="pipe">|</span><span>See Next Lesson Plan</span>
  </div>

  <div class="filed">
    <svg width="15" height="12" viewBox="0 0 15 12"><path d="M0 1 H5 L6 2.5 H13 V11 H0 Z" fill="#9a9a9a"/></svg>Filed Under: Lesson Plans, Science
    <svg width="13" height="13" viewBox="0 0 13 13" style="margin-left:4px"><path d="M0 0 H6 L13 7 L7 13 L0 6 Z" fill="#9a9a9a"/><circle cx="3" cy="3" r="1.2" fill="var(--paper)"/></svg>Tagged With: measurement, science
  </div>

  <footer class="site-footer">
    <span class="social-dot" style="left:118px"></span>
    <span class="social-dot" style="left:156px"></span>
    <span class="social-dot" style="left:195px"></span>
    <span class="footer-brand">thebrightnook</span>
    <span class="copyright">Copyright © thebrightnook 2016</span>
  </footer>
</body>
</html>
```